brightleafwell.com and taverclinic.com

I'd like to do a web design re-make on two of our websites. Brightleafwell.com is focused on selling nutriceutical products (private labeled by brightleafwell.com), and provide an expert blog to give great advices on general health.

Taverclinic.com is a site for Dr. Taver's new medicine clinic. It should be integrated with brightleafwell.com. Clients can directly make appointments on the site, and order products from brightleafwell.com.

Target Market(s)

Middle to upper

Industry/Entity Type

Clinic

Number of Pages Required

4 page

Font styles to use
Serif
Sans Serif

Colors
0254a3
0792cd
33a6d7
00a98f
33b7a4
acd036
9bcb3c
cadf82

Requirements
Must have
• Home page tabs: About Dr. Taver, Store, Blog, Videos, Appointment
• Home page content should include: a promotional section (with moving features), an appointment book (for online appointment booking), a product section (for store), and a blog section.
Nice to have
• The look and feel should be modern, professional, trustworthy, zen.
Should not have
• Real pictures of people, except for Dr. Taver.

```html
<!DOCTYPE html>
<html lang="en">
<head>
<meta charset="utf-8">
<title>Taver Clinic — Blog and Appointment</title>
<link href="https://fonts.googleapis.com/css2?family=Pacifico&family=Signika:wght@400;600&display=swap" rel="stylesheet">
<style>
  :root {
    --page-bg: #ffffff;
    --text-body: #4a4a4a;
    --text-meta: #b5b5b5;
    --rule: #e4e4e4;
    --button: #93c795;
    --button-text: #ffffff;
    --booking-bg: #2e3f52;
    --booking-circle: #33475d;
    --booking-text: #f2f2f2;
    --footer-bg: #25384d;
    --footer-text: #435c77;
  }
  * { margin: 0; padding: 0; box-sizing: border-box; }
  html, body { width: 1200px; height: 717px; overflow: hidden; background: var(--page-bg); }
  body { font-family: "Signika", sans-serif; position: relative; }

  .blog-posts { position: absolute; top: 0; left: 0; width: 1200px; height: 293px; }
  .post {
    position: absolute; width: 240px; text-align: center;
  }
  .post-meta {
    position: absolute; top: -7px; left: 0; width: 240px;
    font-size: 9px; color: var(--text-meta); line-height: 12px;
  }
  .post-rule { position: absolute; top: 18px; left: 0; width: 240px; border-top: 1px solid var(--rule); }
  .post-excerpt {
    position: absolute; top: 29px; left: -6px; width: 252px;
    font-size: 13px; line-height: 16.8px; color: var(--text-body);
  }
  .read-more {
    position: absolute; top: 155px; left: 52px; width: 134px; height: 51px;
    background: var(--button); color: var(--button-text);
    font-size: 14px; line-height: 51px; text-transform: uppercase; text-decoration: none;
  }

  .booking {
    position: absolute; top: 293px; left: 0; width: 1200px; height: 372px;
    background: var(--booking-bg); overflow: hidden; text-align: center; color: var(--booking-text);
  }
  .booking-circle {
    position: absolute; left: 358px; top: -45px; width: 484px; height: 484px;
    border-radius: 50%; background: var(--booking-circle);
  }
  .booking-title {
    position: absolute; top: 16px; left: 0; width: 1200px;
    font-family: "Pacifico", cursive; font-weight: 400; font-size: 28px; line-height: 50px; color: #fff;
  }
  .booking-step {
    position: absolute; top: 102px; left: 0; width: 1200px; font-size: 17px; line-height: 22px;
  }
  .date-picker { position: absolute; top: 139px; left: 574px; width: 50px; height: 51px; }
  .booking-confirm {
    position: absolute; top: 273px; left: 0; width: 1200px; font-size: 17px; line-height: 22px; font-weight: 600;
  }
  .confirm-button {
    position: absolute; top: 321px; left: 0; width: 1200px;
    font-family: "Pacifico", cursive; font-size: 19px; line-height: 30px; color: #fff;
  }

  .site-footer {
    position: absolute; top: 665px; left: 0; width: 1200px; height: 52px;
    background: var(--footer-bg); color: var(--footer-text);
    font-size: 12.5px; line-height: 52px; text-align: center; padding-left: 30px;
  }
</style>
</head>
<body>
  <section class="blog-posts">
    <article class="post" style="left:130px">
      <p class="post-meta">December 17th, 2014 / by Dr.Taver</p>
      <div class="post-rule"></div>
      <p class="post-excerpt">Lorem ipsum dolor sit amet, consectetur adipiscing elit. Duis efficitur volutpat maximus. Sed vitae auctor metus, id fermentum turpis. Etiam vitae dui quis dolor hendrerit pharetra et vel nulla. Fusce volutpat id risus at interdum.</p>
      <a class="read-more" href="#">Read more</a>
    </article>
    <article class="post" style="left:480px;top:-1px">
      <p class="post-meta">December 17th, 2014 / by Dr.Taver</p>
      <div class="post-rule"></div>
      <p class="post-excerpt">Lorem ipsum dolor sit amet, consectetur adipiscing elit. Duis efficitur volutpat maximus. Sed vitae auctor metus, id fermentum turpis. Etiam vitae dui quis dolor hendrerit pharetra et vel nulla. Fusce volutpat id risus at interdum.</p>
      <a class="read-more" href="#">Read more</a>
    </article>
    <article class="post" style="left:830px">
      <p class="post-meta">December 17th, 2014 / by Dr.Taver</p>
      <div class="post-rule"></div>
      <p class="post-excerpt">Lorem ipsum dolor sit amet, consectetur adipiscing elit. Duis efficitur volutpat maximus. Sed vitae auctor metus, id fermentum turpis. Etiam vitae dui quis dolor hendrerit pharetra et vel nulla. Fusce volutpat id risus at interdum.</p>
      <a class="read-more" href="#">Read more</a>
    </article>
  </section>

  <section class="booking">
    <div class="booking-circle"></div>
    <h2 class="booking-title">Take an appointement</h2>
    <p class="booking-step">pick a date</p>
    <svg class="date-picker" viewBox="0 0 50 51" aria-label="Calendar">
      <rect x="2" y="6" width="46" height="43" rx="5" fill="none" stroke="#f2f2f2" stroke-width="3"/>
      <rect x="2" y="6" width="46" height="11" rx="4" fill="#f2f2f2"/>
      <rect x="11" y="1" width="5" height="11" rx="2" fill="#f2f2f2" stroke="#33475d" stroke-width="1.5"/>
      <rect x="34" y="1" width="5" height="11" rx="2" fill="#f2f2f2" stroke="#33475d" stroke-width="1.5"/>
      <text x="25" y="41" text-anchor="middle" font-family="Signika, sans-serif" font-size="21" fill="#f2f2f2">15</text>
    </svg>
    <p class="booking-confirm">So, you choose december 17th, 2014 at 14:45. Right ?</p>
    <p class="confirm-button">Right</p>
  </section>

  <footer class="site-footer">All Contents Copyright © www.Brightleafwell.com. All rights reserved.</footer>
</body>
</html>
```